tazelbox

I would like a label that would print outside of 24oz cups in Orange. The main ingredient for the cups will be noodles. Just like my lumbix projects, I would accept any funky, creative, funny and well noticed labels. Please keep in mind that we are a Korean food joint.

```html
<!DOCTYPE html>
<html lang="en">
<head>
<meta charset="utf-8">
<title>Kimvoro Noodles Cup Label</title>
<link rel="stylesheet" href="https://fonts.googleapis.com/css2?family=Montserrat:wght@600&display=swap">
<style>
  :root {
    --backdrop: #5468a0;
    --cream: #fbe4c9;
    --leaf-green: #2f6f47;
    --paper-white: #ffffff;
    --ink: #141414;
    --veg-orange: rgba(242, 150, 40, 0.85);
    --veg-yellow: rgba(245, 205, 40, 0.85);
    --veg-red: rgba(214, 45, 40, 0.85);
    --veg-tan: rgba(200, 165, 130, 0.85);
    --veg-green: rgba(120, 175, 60, 0.8);
    --veg-purple: rgba(110, 40, 90, 0.8);
  }
  html, body {
    margin: 0;
    padding: 0;
    width: 730px;
    height: 1200px;
    overflow: hidden;
    background: var(--backdrop);
  }
  .canvas {
    position: relative;
    width: 730px;
    height: 1200px;
  }
  .cup-label {
    position: absolute;
    left: 65px;
    top: 298px;
    width: 600px;
    height: 610px;
    box-shadow: 6px 8px 14px rgba(20, 30, 60, 0.35);
    overflow: hidden;
    background: var(--cream);
  }
  .center-band {
    position: absolute;
    left: 126px;
    width: 348px;
    top: 0;
    height: 100%;
    background: var(--leaf-green);
  }
  .veg-art {
    position: absolute;
    background: radial-gradient(closest-side, var(--tone) 0%, var(--tone) 55%, transparent 100%);
  }
  .veg-art--onion    { --tone: var(--veg-orange); left: -20px; top: 60px;  width: 170px; height: 150px; }
  .veg-art--mushroom { --tone: var(--veg-tan);    left: 0;     top: 205px; width: 110px; height: 110px; }
  .veg-art--pepper   { --tone: var(--veg-yellow); left: -10px; top: 360px; width: 140px; height: 150px; }
  .veg-art--cucumber { --tone: var(--veg-green);  left: 0;     top: 520px; width: 130px; height: 100px; }
  .veg-art--chili    { --tone: var(--veg-red);    left: 470px; top: 0;     width: 140px; height: 120px; }
  .veg-art--leek     { --tone: var(--veg-green);  left: 480px; top: 150px; width: 120px; height: 150px; }
  .veg-art--eggplant { --tone: var(--veg-purple); left: 500px; top: 300px; width: 100px; height: 110px; }
  .veg-art--carrot   { --tone: var(--veg-orange); left: 480px; top: 420px; width: 130px; height: 190px; }
  .veg-art--band-top { --tone: rgba(210, 120, 60, 0.55); left: 150px; top: 0;   width: 300px; height: 100px; }
  .veg-art--band-low { --tone: rgba(140, 190, 70, 0.6);  left: 126px; top: 530px; width: 348px; height: 90px; }
  .brand-seal {
    position: absolute;
    left: 50%;
    top: 50%;
    width: 400px;
    height: 400px;
    margin: -200px 0 0 -200px;
    border-radius: 50%;
    background: var(--paper-white);
    overflow: hidden;
  }
  .seal-ring {
    position: absolute;
    inset: 14px;
    border: 2.5px dashed var(--leaf-green);
    border-radius: 50%;
  }
  .brand-dot {
    position: absolute;
    left: 150px;
    top: 45px;
    width: 100px;
    height: 100px;
    border-radius: 50%;
    background: var(--ink);
  }
  .brand-name {
    position: absolute;
    left: 0;
    right: 0;
    top: 190px;
    text-align: center;
    font-family: "Montserrat", sans-serif;
    font-weight: 600;
    font-size: 60px;
    line-height: 72px;
    letter-spacing: -1px;
    color: var(--ink);
    margin: 0;
  }
  .product-banner {
    position: absolute;
    left: 0;
    right: 0;
    top: 284px;
    height: 60px;
    background: var(--leaf-green);
    display: flex;
    align-items: center;
    justify-content: center;
    font-family: "Montserrat", sans-serif;
    font-weight: 600;
    font-size: 32px;
    letter-spacing: 1px;
    color: var(--paper-white);
  }
</style>
</head>
<body>
<main class="canvas">
  <section class="cup-label">
    <div class="center-band"></div>
    <div class="veg-art veg-art--onion" role="img" aria-label="Illustrated onion with spring onion stalk"></div>
    <div class="veg-art veg-art--mushroom" role="img" aria-label="Illustrated mushroom"></div>
    <div class="veg-art veg-art--pepper" role="img" aria-label="Illustrated yellow bell pepper"></div>
    <div class="veg-art veg-art--cucumber" role="img" aria-label="Illustrated cucumber"></div>
    <div class="veg-art veg-art--chili" role="img" aria-label="Illustrated red chili pepper"></div>
    <div class="veg-art veg-art--leek" role="img" aria-label="Illustrated leek"></div>
    <div class="veg-art veg-art--eggplant" role="img" aria-label="Illustrated eggplant"></div>
    <div class="veg-art veg-art--carrot" role="img" aria-label="Illustrated carrot"></div>
    <div class="veg-art veg-art--band-top" role="img" aria-label="Small illustrated potato, pea pod, tomato and flower"></div>
    <div class="veg-art veg-art--band-low" role="img" aria-label="Small illustrated tomato, salt shaker, pea pod, broccoli and beetroot"></div>
    <div class="brand-seal">
      <div class="seal-ring"></div>
      <div class="brand-dot"></div>
      <h1 class="brand-name">Kimvoro</h1>
      <div class="product-banner">NOODLES</div>
    </div>
  </section>
</main>
</body>
</html>
```